Brisk Hollow Builders Needs A Flyer

We need a flyer for our newest product "The Cedarlane Garden Workroom"

Here is some copy for the flyer:

1. More and more people everyday are working from home and finding it difficult to disconnect from home activities in order to focus on their work. They are also finding it very expensive to add on to their existing house for a quiet place. Our archatectually stunning, Cedarlane Garden Workroom is the answer. The office studio measures 16' wide and 10' deep. 160 Square feet of space.

Perfect for dozens of purposes. Home office, design studio, artist studio, home school office, reading room, craft studio, drafting room.

Features include:

- Steel Framing. 40-60% lighter then wood, higher strength to weight ratio, resistant to mold and fire and steel is the most recycled material on earth!
- Spray foam insulation. Cool in the summer and warm in the winter.
- HVAC Mini Split with wireless remote control and thermostat.
- 100% Off grid with enough solar and battery storage to run your entire office. No need to pay for an expensive electric installation.
- Flush fitting floor outlets to reduce wires.
- TV mount (Optional with pre-wired electric, HDMI, digital audio & Cat 6)
- Windows are tempered glass custom made by Morvik Glazing.
- Solar qualifies for a 26% tax credit. This is not a write-off rather it is a direct reduction on your tax obligation.
- Thousands of dollars less than adding onto your home.
- Custom color, siding, features available.

This beautiful back yard office is delivered 100% assembled and ready to enjoy on the day of delivery.

We ship nationwide from our factory in South Carolina. Give us a call anytime to speak to a designer and start your dream office today!

555-318-4027
info@BriskHollowBuilders.example

```html
<!DOCTYPE html>
<html lang="en">
<head>
<meta charset="utf-8">
<title>Brisk Hollow Builders — The Cedarlane Garden Workroom</title>
<link rel="stylesheet" href="https://fonts.googleapis.com/css2?family=Oswald:wght@500;700&family=Open+Sans:wght@400;600;700&display=swap">
<style>
  :root{
    --forest:#1f4a2b;
    --forest-deep:#183d23;
    --leaf:#8cc540;
    --amber:#f4a11b;
    --ink:#333a35;
    --paper:#ffffff;
    --mist:#e9efe6;
  }
  *{margin:0;padding:0;box-sizing:border-box}
  html,body{width:849px;height:1200px;overflow:hidden;background:var(--paper)}
  body{font-family:"Open Sans",Arial,sans-serif;color:var(--ink);position:relative}
  .flyer{position:relative;width:849px;height:1200px}

  .brand{position:absolute;left:40px;top:26px;display:flex;align-items:center;gap:12px}
  .brand-dot{width:46px;height:46px;border-radius:50%;background:var(--amber)}
  .brand-name{font-family:"Oswald",sans-serif;font-weight:700;font-size:26px;line-height:1;color:var(--forest);text-transform:uppercase;letter-spacing:.5px}

  .social{position:absolute;right:36px;top:28px;display:flex;gap:18px}
  .social-item{display:flex;align-items:center;gap:6px;font-size:10.5px;color:var(--ink)}
  .social-item span.mark{width:16px;height:16px;border-radius:50%;background:var(--forest)}

  .headline{position:absolute;left:0;right:0;top:104px;text-align:center;font-family:"Oswald",sans-serif;font-weight:700;text-transform:uppercase;line-height:1.02}
  .headline .top{display:block;font-size:58px;color:var(--forest)}
  .headline .bottom{display:block;font-size:62px;color:var(--amber)}

  .intro{position:absolute;top:250px;left:40px;width:500px;display:grid;grid-template-columns:1fr 1fr;gap:20px;font-size:12.2px;line-height:1.5}
  .intro p+p{margin-top:10px}
  .intro-photo{position:absolute;top:248px;left:560px;width:252px;height:160px;background:linear-gradient(135deg,#b9cbd4 0%,#6f7d6a 55%,#3f4a38 100%)}

  .features{position:absolute;top:422px;left:0;width:849px;height:628px;background:var(--forest)}
  .features-band{position:absolute;top:0;left:0;width:100%;height:58px;background:var(--forest-deep);display:flex;align-items:center;justify-content:center}
  .features-band h2{font-family:"Oswald",sans-serif;font-weight:700;font-size:30px;color:var(--amber);letter-spacing:1px;text-transform:uppercase}
  .hero-circle{position:absolute;left:311px;top:132px;width:240px;height:240px;border-radius:50%;background:radial-gradient(circle at 50% 40%,#dfe6e2 0%,#9aa89a 55%,#56654f 100%);border:6px solid var(--leaf)}
  .links{position:absolute;left:0;top:0}

  .feature{position:absolute;width:225px;color:#fff;font-size:10.5px;line-height:1.42}
  .feature h3{font-family:"Oswald",sans-serif;font-weight:700;font-size:15px;color:var(--leaf);text-transform:uppercase;letter-spacing:.4px;line-height:1.2;margin-bottom:2px}
  .feature.left{left:40px;text-align:right}
  .feature.right{left:600px;width:215px}
  .icon{position:absolute;width:40px;height:40px;border-radius:50%;background:var(--amber);display:flex;align-items:center;justify-content:center}
  .icon svg{width:22px;height:22px}

  .closing{position:absolute;top:1050px;left:0;width:849px;height:110px}
  .badge{position:absolute;left:40px;top:17px;width:76px;height:76px;border-radius:50%;border:3px solid var(--leaf);display:flex;flex-direction:column;align-items:center;justify-content:center;font-family:"Oswald",sans-serif;color:var(--forest);text-transform:uppercase}
  .badge b{font-size:22px;line-height:1}
  .badge small{font-size:9px;letter-spacing:.5px}
  .closing-copy{position:absolute;left:136px;top:12px;width:320px;font-size:10.8px;line-height:1.4}
  .closing-copy p+p{margin-top:5px}
  .closing-copy strong{color:var(--forest)}
  .closing-photo{position:absolute;left:470px;top:15px;width:340px;height:80px;background:linear-gradient(120deg,#c9d6c0 0%,#7d8f6d 50%,#4d5c42 100%)}

  .footer{position:absolute;left:0;bottom:0;width:849px;height:40px;background:var(--forest);color:#fff;display:flex;align-items:center;justify-content:center;font-size:11.5px;letter-spacing:.3px}
</style>
</head>
<body>
<div class="flyer">

  <header>
    <div class="brand"><span class="brand-dot"></span><span class="brand-name">Brisk Hollow Builders</span></div>
    <div class="social">
      <div class="social-item"><span class="mark"></span>@briskhollowbuilders</div>
      <div class="social-item"><span class="mark"></span>@briskhollowbuilders</div>
      <div class="social-item"><span class="mark"></span>@briskhollowbuilders</div>
    </div>
  </header>

  <h1 class="headline"><span class="top">The Cedarlane</span><span class="bottom">Garden Workroom</span></h1>

  <section class="intro">
    <div>
      <p>More and more people everyday are working from home and finding it difficult to disconnect from home activities in order to focus on their work. They are also finding it very expensive to add on to their existing house for a quiet place. Our architecturally stunning, Cedarlane Garden Workroom is the answer.</p>
    </div>
    <div>
      <p>The office studio measures 16' wide and 10' deep. 160 Square feet of space.</p>
      <p>Perfect for dozens of purposes. Home office, design studio, artist studio, home school office, reading room, craft studio, drafting room.</p>
    </div>
  </section>
  <div class="intro-photo" role="img" aria-label="Photo of the garden workroom studio in a backyard"></div>

  <section class="features">
    <div class="features-band"><h2>Features Include</h2></div>

    <svg class="links" width="849" height="628" aria-hidden="true">
      <g stroke="#8cc540" stroke-width="1.5" fill="none">
        <line x1="305" y1="172" x2="350" y2="200"/>
        <line x1="305" y1="288" x2="320" y2="270"/>
        <line x1="305" y1="382" x2="335" y2="330"/>
        <line x1="305" y1="490" x2="370" y2="360"/>
        <line x1="305" y1="581" x2="400" y2="370"/>
        <line x1="545" y1="172" x2="510" y2="200"/>
        <line x1="545" y1="263" x2="540" y2="250"/>
        <line x1="545" y1="356" x2="530" y2="320"/>
        <line x1="545" y1="464" x2="490" y2="365"/>
        <line x1="545" y1="574" x2="460" y2="372"/>
      </g>
    </svg>

    <div class="hero-circle" role="img" aria-label="Photo of the finished garden workroom with glass front"></div>

    <div class="feature left" style="top:140px"><h3>Steel Framing</h3>40-60% lighter than wood, higher strength to weight ratio, resistant to mold and fire and steel is the most recycled material on earth!</div>
    <div class="icon" style="left:270px;top:152px"><svg viewBox="0 0 24 24" fill="none" stroke="#fff" stroke-width="2"><path d="M3 20h18M6 20V8h12v12M6 8l6-5 6 5"/></svg></div>

    <div class="feature left" style="top:258px"><h3>Spray Foam Insulation</h3>Cool in the summer and warm in the winter.</div>
    <div class="icon" style="left:270px;top:268px"><svg viewBox="0 0 24 24" fill="none" stroke="#fff" stroke-width="2"><path d="M12 3v14M8 7l4-4 4 4"/><circle cx="12" cy="19" r="2"/></svg></div>

    <div class="feature left" style="top:352px"><h3>HVAC Mini Split</h3>With wireless remote control and thermostat</div>
    <div class="icon" style="left:270px;top:362px"><svg viewBox="0 0 24 24" fill="none" stroke="#fff" stroke-width="2"><rect x="3" y="6" width="18" height="8" rx="2"/><path d="M7 18h2M11 18h2M15 18h2"/></svg></div>

    <div class="feature left" style="top:458px"><h3>Flush Fitting<br>Floor Outlets</h3>To reduce wires</div>
    <div class="icon" style="left:270px;top:470px"><svg viewBox="0 0 24 24" fill="none" stroke="#fff" stroke-width="2"><rect x="5" y="4" width="14" height="16" rx="2"/><path d="M10 9v3M14 9v3M10 16h4"/></svg></div>

    <div class="feature left" style="top:552px"><h3>Custom Color, Siding</h3>Features available</div>
    <div class="icon" style="left:270px;top:561px"><svg viewBox="0 0 24 24" fill="none" stroke="#fff" stroke-width="2"><path d="M4 20l6-6M14 4l6 6-8 8-6-6z"/></svg></div>

    <div class="feature right" style="top:140px"><h3>TV Mount</h3>(Optional with pre-wired electric, HDMI, digital audio &amp; Cat 6)</div>
    <div class="icon" style="left:545px;top:152px"><svg viewBox="0 0 24 24" fill="none" stroke="#fff" stroke-width="2"><rect x="3" y="5" width="18" height="12" rx="1"/><path d="M9 21h6M12 17v4"/></svg></div>

    <div class="feature right" style="top:232px"><h3>Windows</h3>Are tempered glass custom made by Morvik Glazing</div>
    <div class="icon" style="left:545px;top:243px"><svg viewBox="0 0 24 24" fill="none" stroke="#fff" stroke-width="2"><rect x="4" y="4" width="16" height="16"/><path d="M12 4v16M4 12h16"/></svg></div>

    <div class="feature right" style="top:322px"><h3>Solar Qualifies</h3>For a 26% tax credit. This is not a write-off rather it is a direct reduction on your tax obligation.</div>
    <div class="icon" style="left:545px;top:336px"><svg viewBox="0 0 24 24" fill="none" stroke="#fff" stroke-width="2"><circle cx="12" cy="12" r="4"/><path d="M12 2v3M12 19v3M2 12h3M19 12h3M5 5l2 2M17 17l2 2M5 19l2-2M17 7l2-2"/></svg></div>

    <div class="feature right" style="top:430px"><h3>Thousands of Dollars</h3>Less than adding onto your home</div>
    <div class="icon" style="left:545px;top:444px"><svg viewBox="0 0 24 24" fill="none" stroke="#fff" stroke-width="2"><path d="M16 7c-1-1-2.5-1.5-4-1.5-2 0-3.5 1-3.5 2.8 0 3.7 7.5 2 7.5 6 0 1.8-1.6 3-4 3-1.6 0-3-.6-4-1.6M12 3v3M12 18v3"/></svg></div>

    <div class="feature right" style="top:530px"><h3>100% Off Grid</h3>With enough solar and battery storage to run your entire office. No need to pay for an expensive electric installation.</div>
    <div class="icon" style="left:545px;top:554px"><svg viewBox="0 0 24 24" fill="none" stroke="#fff" stroke-width="2"><path d="M13 2L5 14h6l-1 8 8-12h-6z"/></svg></div>
  </section>

  <section class="closing">
    <div class="badge"><b>100%</b><small>Assembled</small></div>
    <div class="closing-copy">
      <p>This beautiful back yard office is delivered 100% assembled and ready to enjoy on the day of delivery.</p>
      <p><strong>We ship nationwide from our factory in South Carolina.</strong></p>
      <p>Give us a call anytime to speak to a designer and start your dream office today!</p>
    </div>
    <div class="closing-photo" role="img" aria-label="Photo of the garden workroom at dusk with lights on"></div>
  </section>

  <footer class="footer">2150 Fernridge Rd, Lakemont, SC 29000 &nbsp;|&nbsp; 555-318-4027 &nbsp;|&nbsp; info@BriskHollowBuilders.example</footer>
</div>
</body>
</html>
```